Spice Mix Label Bottle Branding - Health and Weight Loss Mixes

The company is called ZestoLane Spice Mix's. We've created 5 spice mixes using ingredients that promote health and weight loss. We already have a logo but now we need labels for our bottles. We would like to see designs that have the feel of health supplements (see attached examples)

We would like a different colour featured with each of our flavours.

Our flavours are:
-Golden Chai (Yellow)
-Mild Curry (Orange)
-Coffee Rub (brown)
-Garlic Oregano (Green)
-Taco (Blue)

Thank you!

Target Market(s)

Ages 22-35. Men and Female. Trendy, Hipster.

Industry/Entity Type

Food Production

Font styles to use
Sans Serif

Colors
f37122
0655a3
0692cd
9bcb3c
fbee3f

Requirements
Must have
• A different featured colour for each flavour.
• The ZestoLane Spices Logo (attached)
• The slogan: "Weight Loss Ingredients"
• -Golden Chai (Yellow)
• -Mild Curry (Orange)
• -Coffee Rub (brown)
• -Garlic Oregano (Green)
• -Taco (Blue)
• Text Files attached.
Nice to have
• A black label with a featured colour for each of the spice mice flavours.
• 'No Salt added'

```html
<!DOCTYPE html>
<html lang="en">
<head>
<meta charset="utf-8">
<title>ZestoLane Spices – Mild Curry Label</title>
<link rel="stylesheet" href="https://fonts.googleapis.com/css2?family=Montserrat:wght@800&family=Oswald:wght@500;600&display=swap">
<style>
  :root {
    --backdrop: #e6e6e6;
    --label-dark: #221f1f;
    --label-mid: #3a3535;
    --flavour: #f37122;
    --ink-light: #ffffff;
    --ink-dark: #1a1717;
    --art-tone: #5a5454;
  }
  html, body {
    margin: 0;
    width: 953px;
    height: 1200px;
    overflow: hidden;
    background: var(--backdrop);
  }
  .label {
    position: absolute;
    left: 26px;
    top: 77px;
    width: 900px;
    height: 1046px;
    background: linear-gradient(90deg, var(--label-dark) 0%, var(--label-mid) 45%, var(--label-mid) 55%, var(--label-dark) 100%);
    font-family: "Montserrat", sans-serif;
    color: var(--ink-light);
  }
  .brand {
    position: absolute;
    top: 150px;
    left: 0;
    right: 0;
    display: flex;
    justify-content: center;
    align-items: center;
    gap: 18px;
  }
  .brand-dot {
    width: 26px;
    height: 26px;
    border-radius: 50%;
    background: var(--flavour);
  }
  .brand-name {
    font-family: "Montserrat", sans-serif;
    font-weight: 800;
    font-size: 60px;
    letter-spacing: 1px;
    color: var(--ink-light);
  }
  .flavour-name {
    position: absolute;
    top: 325px;
    left: 0;
    right: 0;
    margin: 0;
    text-align: center;
    font-family: "Montserrat", sans-serif;
    font-weight: 800;
    font-size: 126px;
    line-height: 140px;
    color: var(--flavour);
    letter-spacing: 2px;
  }
  .flavour-art {
    position: absolute;
    top: 620px;
    left: 320px;
    width: 260px;
    height: 180px;
    border-radius: 12px;
    background: radial-gradient(ellipse at center, var(--art-tone) 0%, rgba(90,84,84,0) 75%);
  }
  .slogan {
    position: absolute;
    top: 838px;
    left: 0;
    right: 0;
    margin: 0;
    text-align: center;
    font-family: "Oswald", sans-serif;
    font-weight: 600;
    font-variant: small-caps;
    font-size: 48px;
    line-height: 60px;
    letter-spacing: 1px;
    color: var(--ink-light);
  }
  .salt-band {
    position: absolute;
    top: 918px;
    left: 0;
    right: 0;
    height: 68px;
    background: var(--flavour);
    display: flex;
    align-items: center;
    justify-content: center;
  }
  .salt-note {
    font-family: "Oswald", sans-serif;
    font-weight: 500;
    font-size: 28px;
    letter-spacing: 0.5px;
    color: var(--ink-dark);
  }
</style>
</head>
<body>
  <section class="label">
    <div class="brand">
      <span class="brand-dot"></span>
      <span class="brand-name">ZestoLane Spices</span>
    </div>
    <h1 class="flavour-name">MILD<br>CURRY</h1>
    <div class="flavour-art" role="img" aria-label="Line drawing of a steaming cup with leaves"></div>
    <p class="slogan">Weight Loss Ingredients</p>
    <div class="salt-band">
      <span class="salt-note">NO SALT ADDED</span>
    </div>
  </section>
</body>
</html>
```